Corporate Design für junge Steuerberater
Zielgruppe
Wir sind eine junge Steuerberatungsgesellschaft (2 jünge Mütter). Unsere Kunden sind überwiegend kleine Unternehmer
Aufgabenstellung
Logo und Geschäftspapiere sollen leger, aber seriös wirken.
Wir benötigen ein Logo, Visitenkarten, Briefpapier bzw. Deckblätter für unsere Bilanzen, Steuererklärungen. Deckblätter und Briefpapier können auch gleich aussehen.
(Das Beispielbild ist natürlich nicht von unserem Unternehmen, würde uns vom Stil her gut gefallen....ist aber kein Muss)

```html
<!DOCTYPE html>
<html lang="de">
<head>
<meta charset="utf-8">
<title>KTR Steuerberatung – Deckblatt Jahresabschluss</title>
<link href="https://fonts.googleapis.com/css2?family=Roboto:wght@400;500;700&family=Montserrat:wght@400&display=swap" rel="stylesheet">
<style>
  :root {
    --teal: #5a9b98;
    --teal-faint: #d7e5e5;
    --ink: #2a2a2a;
    --paper: #ffffff;
    --backdrop: #eeeeec;
  }
  * { margin: 0; padding: 0; box-sizing: border-box; }
  html, body {
    width: 1200px; height: 1200px; overflow: hidden;
    background: var(--backdrop);
  }
  .sheet {
    position: absolute; left: 190px; top: 20px;
    width: 820px; height: 1160px;
    background: var(--paper);
    overflow: hidden;
    font-family: "Roboto", Arial, sans-serif;
  }
  .brand {
    position: absolute; left: 0; right: 0; top: 62px;
    text-align: center; color: var(--teal);
  }
  .brand-name {
    display: block; font-weight: 700; font-size: 54px; line-height: 1;
    letter-spacing: 0.04em;
  }
  .brand-line {
    display: block; margin-top: 8px; margin-left: 120px;
    font-weight: 400; font-size: 11.5px; letter-spacing: 0.16em;
  }
  .backdrop-mark {
    position: absolute; left: -20px; top: 622px;
    font-weight: 700; font-size: 480px; line-height: 1;
    color: var(--teal-faint); letter-spacing: -0.02em;
    white-space: nowrap; user-select: none;
  }
  .doc-title {
    position: absolute; left: 78px; top: 446px;
    color: var(--teal); font-weight: 700; font-size: 22px;
    letter-spacing: 0.78em;
  }
  .doc-meta {
    position: absolute; left: 78px; color: var(--teal);
    font-weight: 500; font-size: 12.5px;
  }
  .doc-date { top: 534px; }
  .doc-firm { top: 566px; }
  .client-address {
    position: absolute; left: 78px; top: 605px;
    font-family: "Montserrat", Arial, sans-serif; font-style: normal;
    font-size: 12.2px; line-height: 17px; color: var(--ink);
  }
  .sheet-footer {
    position: absolute; left: 0; right: 0; top: 1055px;
    text-align: center; color: var(--ink);
    font-size: 8.6px; line-height: 13.5px;
  }
</style>
</head>
<body>
  <main class="sheet">
    <div class="backdrop-mark" aria-hidden="true">KTR</div>

    <header class="brand">
      <span class="brand-name">KTR</span>
      <span class="brand-line">STEUERBERATUNG</span>
    </header>

    <h1 class="doc-title">JAHRESABSCHLUSS</h1>
    <p class="doc-meta doc-date">auf den 31. Dezember 2022</p>
    <p class="doc-meta doc-firm">der Firma</p>

    <address class="client-address">
      Jonas Beispiel<br>
      Musterstraße 12<br>
      12345 Musterhausen
    </address>

    <footer class="sheet-footer">
      <p>Musterstr. 22 | 12345 Musterhausen fon +49 30 9876540 fax +49 30 9876541 mail. info@ktr-steuerberatung.de web. ktr-steuerberatung.de</p>
      <p>St- Id. Nr. 9876543210 | USt.-Nr. 31245678901 | Beispiel Bank | IBAN DE00 1234 5678 9012 3456 78 | SWIFT-BIC BEISDEXXXXX</p>
    </footer>
  </main>
</body>
</html>
```